small auto electrical company needs new logo and business cards !!!

we are a small auto electrical company (Velmor Autos Ltd) that has been running for 13 years the logo we have was put together by dinosaurs so we are looking at re branding the company starting with business cards and a new logo we fit GPS tracking devices for young drivers through there insurance company also we fit hands free systems and dash cameras also safety locks to fleet vehicles we would like bright eye catching colours day glow and neon and quirky designs for the logo our original logo was baby blue which i have added a picture enclosed we would like double sided but have a space to write notes and prices preferably not white on back same colour throughout many thanks
Reason: Just a chance to finalise any designs we want VA logos or V logos - No vlm's and no dinosaurs lol
Business
Installs@velmorautos.co.uk
07922483617
www.Velmorautos.co.uk
Velmor Autos Ltd - Fleets and Insurance Services
- new logo design !!
- Satellite in logo or something attaining to gps
- maybe a car in the logo
- shouldnt have velmor as vlm it is VeLMOR Autos

```html
<!DOCTYPE html>
<html lang="en">
<head>
<meta charset="utf-8">
<title>Velmor Autos Ltd – Business Cards</title>
<link rel="stylesheet" href="https://fonts.googleapis.com/css2?family=Exo+2:wght@500;600&family=Saira+Extra+Condensed:wght@500;600&family=Oswald:wght@500&display=swap">
<style>
  :root {
    --page: #ffffff;
    --purple: #662766;
    --sky: #45c3ef;
    --orange: #f15a24;
    --green: #8cc63f;
    --yellow: #fcee21;
    --badge: #1f86c8;
    --silver-light: #f2f2f2;
    --silver-mid: #9a9a9a;
    --silver-dark: #111111;
    --brand-font: "Saira Extra Condensed", "Oswald", "Arial Narrow", sans-serif;
    --body-font: "Exo 2", sans-serif;
  }
  * { margin: 0; padding: 0; box-sizing: border-box; }
  html, body {
    width: 1200px; height: 900px; overflow: hidden;
    background: var(--page);
  }
  .canvas { position: relative; width: 1200px; height: 900px; }

  .card {
    position: absolute;
    width: 505px; height: 290px;
    background: var(--purple);
    overflow: hidden;
  }
  .card--front { left: 357px; top: 90px; }
  .card--back  { left: 337px; top: 553px; }

  .card__wave { position: absolute; left: 0; width: 505px; height: 80px; }
  .card--front .card__wave { top: 0; }
  .card--back  .card__wave { bottom: 0; }

  /* small brand mark, front */
  .brand-small {
    position: absolute; top: 8px; right: 12px;
    display: flex; align-items: center; gap: 4px;
    white-space: nowrap;
  }
  .brand-small__dot {
    width: 22px; height: 22px; border-radius: 50%;
    background: var(--sky); flex: none;
  }
  .brand-small__text {
    font-family: var(--brand-font);
    font-weight: 600; color: var(--sky);
    line-height: 1;
  }
  .brand-small__name { font-size: 14px; display: block; letter-spacing: 0.5px; }
  .brand-small__tag  { font-size: 7px; display: block; letter-spacing: 0.3px; margin-top: 1px; }

  .offer__title {
    position: absolute; left: 38px; top: 78px;
    font-family: var(--body-font); font-weight: 500;
    font-size: 36px; color: var(--orange); line-height: 1;
    white-space: nowrap;
  }
  .offer__list {
    position: absolute; left: 40px; top: 140px;
    list-style: none;
    font-family: var(--body-font); font-weight: 500;
    font-size: 25px; color: var(--green); line-height: 28px;
    white-space: nowrap;
  }
  .offer__list li { display: flex; align-items: center; gap: 8px; }
  .offer__list li::before {
    content: ""; width: 12px; height: 12px; border-radius: 50%;
    background: var(--orange); flex: none;
  }

  .experience-badge {
    position: absolute; left: 331px; top: 96px;
    width: 156px; height: 63px;
    background: var(--badge); border-radius: 8px;
    box-shadow: 0 10px 14px -4px rgba(230, 170, 255, 0.75);
    display: flex; flex-direction: column; align-items: center; justify-content: center;
    font-family: var(--body-font); font-weight: 600;
    color: var(--yellow); line-height: 1;
    white-space: nowrap;
  }
  .experience-badge__years { font-size: 27px; letter-spacing: 0.5px; }
  .experience-badge__label { font-size: 20px; margin-top: 2px; }

  /* large brand, back */
  .brand-large__dot {
    position: absolute; left: 200px; top: 21px;
    width: 105px; height: 105px; border-radius: 50%;
    background: var(--sky);
  }
  .brand-large__name, .brand-large__tag {
    position: absolute; left: 0; width: 505px; text-align: center;
    font-family: var(--brand-font); font-weight: 600;
    color: var(--sky); line-height: 1;
    white-space: nowrap;
  }
  .brand-large__name { top: 132px; font-size: 48px; letter-spacing: 1px; }
  .brand-large__tag  { top: 184px; font-size: 26px; letter-spacing: 1px; }
</style>
</head>
<body>
<main class="canvas">

  <section class="card card--front" aria-label="Business card front">
    <svg class="card__wave" viewBox="0 0 505 80" aria-hidden="true">
      <defs>
        <linearGradient id="silverTop" x1="0" y1="0" x2="1" y2="0">
          <stop offset="0" stop-color="#f2f2f2"/>
          <stop offset="0.45" stop-color="#9a9a9a"/>
          <stop offset="1" stop-color="#111111"/>
        </linearGradient>
      </defs>
      <path d="M0 0 H505 V32 C420 28 360 10 280 38 C200 62 90 40 0 46 Z" fill="url(#silverTop)"/>
      <path d="M0 46 C90 40 200 62 280 38 C360 10 420 28 505 32" fill="none" stroke="#ffffff" stroke-width="4"/>
    </svg>

    <div class="brand-small">
      <span class="brand-small__dot"></span>
      <span class="brand-small__text">
        <span class="brand-small__name">VELMOR AUTOS LTD</span>
        <span class="brand-small__tag">FLEET &amp; INSURANCE SERVICE</span>
      </span>
    </div>

    <h2 class="offer__title">We offer to fit</h2>
    <ul class="offer__list">
      <li>GPS tracking devices</li>
      <li>Hands free systems</li>
      <li>Dash cameras</li>
      <li>Safety locks</li>
    </ul>

    <div class="experience-badge">
      <span class="experience-badge__years">13 YEARS</span>
      <span class="experience-badge__label">EXPERIENCE</span>
    </div>
  </section>

  <section class="card card--back" aria-label="Business card back">
    <span class="brand-large__dot"></span>
    <h1 class="brand-large__name">VELMOR AUTOS LTD</h1>
    <p class="brand-large__tag">FLEET &amp; INSURANCE SERVICE</p>

    <svg class="card__wave" viewBox="0 0 505 80" aria-hidden="true">
      <defs>
        <linearGradient id="silverBottom" x1="0" y1="0" x2="1" y2="0">
          <stop offset="0" stop-color="#f2f2f2"/>
          <stop offset="0.5" stop-color="#9a9a9a"/>
          <stop offset="1" stop-color="#111111"/>
        </linearGradient>
      </defs>
      <path d="M0 36 C90 26 180 56 270 50 C370 44 430 18 505 22 V80 H0 Z" fill="url(#silverBottom)"/>
      <path d="M0 36 C90 26 180 56 270 50 C370 44 430 18 505 22" fill="none" stroke="#ffffff" stroke-width="4"/>
    </svg>
  </section>

</main>
</body>
</html>
```